Back Pain

Need a flyer similar to the attached draft. This is to be handed out to prospective patients. Note that Sketch Hive has already designed the logo. If you need a copy please contact me

```html
<!DOCTYPE html>
<html lang="en">
<head>
<meta charset="utf-8">
<title>Tech Neck Flyer</title>
<link href="https://fonts.googleapis.com/css2?family=Barlow+Condensed:wght@400;500;600;700;800&display=swap" rel="stylesheet">
<style>
  :root {
    --page: #f2f2f2;
    --ink: #000000;
    --white: #ffffff;
    --lime: #c8e35a;
    --sky: #00b2e3;
    --navy: #0b2b74;
    --navy-deep: #06195a;
    --alert: #ff4a26;
    --ring: #6b6b6b;
    --brand-blue: #1a8fd6;
    --brand-green: #8cc63f;
  }
  * { margin: 0; padding: 0; box-sizing: border-box; }
  html, body { width: 1200px; height: 1200px; overflow: hidden; background: var(--page); }
  body { font-family: "Barlow Condensed", sans-serif; position: relative; }

  .flyer {
    position: absolute; left: 378px; top: 200px;
    width: 589px; height: 883px;
    background: var(--ink); overflow: hidden; color: var(--white);
  }
  .flyer > * { position: absolute; }
  .backdrop { left: 0; top: 0; width: 589px; height: 883px; }

  .brand { left: 0; width: 589px; top: 22px; text-align: center; }
  .brand-mark { width: 86px; height: 86px; border-radius: 50%; border: 5px solid var(--brand-blue); margin: 0 auto 4px; }
  .brand-name { font-weight: 700; font-size: 21px; color: var(--brand-blue); letter-spacing: 0.2px; line-height: 1; }
  .brand-sub { font-weight: 700; font-size: 10px; color: var(--brand-green); letter-spacing: 1.6px; margin-top: 2px; }

  .headline {
    left: 0; width: 589px; top: 150px; text-align: center;
    font-weight: 800; font-size: 92px; line-height: 1; letter-spacing: 1px;
    text-shadow: 3px 3px 0 var(--lime);
  }

  .symptom {
    background: var(--alert); color: var(--white);
    font-size: 13px; letter-spacing: 1px; line-height: 15px; height: 15px;
    text-align: right; padding-right: 4px;
  }

  .illustration { border-radius: 4px; }
  .figure { left: 102px; top: 262px; width: 122px; height: 338px; border-radius: 50px 50px 20px 20px;
    background: linear-gradient(180deg, #f6ead8 0%, #f8f4ee 45%, #2a7fd4 60%, #1d5fc2 100%); }
  .xray { left: 184px; top: 246px; width: 140px; height: 140px; border-radius: 50%;
    background: radial-gradient(circle at 55% 55%, #c8452a 0%, #555 35%, #2a2a2a 80%); }
  .head-icon { left: 266px; top: 356px; width: 80px; height: 80px; border-radius: 50%;
    background: radial-gradient(circle, #ffffff 0%, #0b67b5 55%); }

  .chart-note { left: 339px; top: 320px; font-size: 12px; line-height: 16px; font-weight: 500; color: var(--ink); }
  .chart-note strong { font-weight: 700; }
  .bar-value { font-size: 17px; font-weight: 600; color: var(--white); text-align: center; }
  .degrees { top: 449px; left: 356px; font-size: 18px; font-weight: 600; color: var(--navy-deep); word-spacing: 6px; }
  .axis-label { font-size: 11px; color: var(--ink); font-weight: 500; }
  .axis-x { top: 468px; left: 362px; }
  .axis-y { left: 517px; top: 438px; transform: rotate(-90deg); transform-origin: left top; white-space: nowrap; }

  .usage { left: 354px; top: 502px; color: var(--navy-deep); }
  .usage .small { font-size: 12px; letter-spacing: 1.2px; line-height: 14px; }
  .usage .big { font-size: 21px; font-weight: 600; letter-spacing: 1.4px; line-height: 22px; }

  .message {
    left: 245px; top: 578px; width: 344px; height: 132px;
    background: var(--ink); border-radius: 12px 0 0 12px;
    padding: 15px 0 0 23px;
    font-size: 19.5px; font-weight: 500; letter-spacing: 1.6px; line-height: 20px;
  }
  .message .accent { color: var(--lime); }

  .contact-band { left: 0; top: 670px; width: 589px; height: 178px; background: var(--sky); z-index: -0; }
  .portrait { left: 40px; top: 644px; width: 204px; height: 204px; border-radius: 50%;
    background: radial-gradient(circle at 50% 45%, #e9d3c2 0%, #dfe6ea 55%, #eef2f4 100%); }
  .contact { left: 268px; top: 713px; font-size: 19px; font-weight: 700; line-height: 21.6px; letter-spacing: 0.2px; }

  .footer { left: 0; top: 848px; width: 589px; height: 35px; background: var(--lime); color: var(--ink); }
  .footer span { position: absolute; top: 10px; font-size: 13px; letter-spacing: 1.2px; }
  .footer .cta { left: 66px; }
  .footer .url { left: 269px; font-weight: 700; font-size: 14px; top: 9px; }
</style>
</head>
<body>
<main class="flyer">
  <svg class="backdrop" viewBox="0 0 589 883" aria-hidden="true">
    <circle cx="294" cy="430" r="330" fill="none" stroke="var(--ring)" stroke-width="0.8"/>
    <circle cx="294" cy="430" r="250" fill="none" stroke="var(--ring)" stroke-width="0.8"/>
    <circle cx="294" cy="430" r="180" fill="none" stroke="var(--ring)" stroke-width="0.8"/>
    <circle cx="425" cy="492" r="226" fill="var(--lime)"/>
    <g fill="var(--navy)">
      <rect x="358" y="429" width="22" height="16" rx="3"/>
      <rect x="390" y="394" width="24" height="51" rx="3"/>
      <rect x="422" y="367" width="23" height="78" rx="3"/>
      <rect x="457" y="349" width="23" height="96" rx="3"/>
      <rect x="490" y="328" width="24" height="117" rx="3"/>
    </g>
    <circle cx="323" cy="524" r="24" fill="var(--navy-deep)"/>
    <path d="M323 524 L323 500 A24 24 0 0 1 341 540 Z" fill="var(--sky)"/>
  </svg>

  <header class="brand">
    <div class="brand-mark"></div>
    <div class="brand-name">SPINEWELL CARE CLINIC</div>
    <div class="brand-sub">DR SAM HARLOW - CHIROPRACTOR</div>
  </header>

  <h1 class="headline">TECH NECK</h1>

  <div class="illustration figure" role="img" aria-label="Illustrated man with hands on his sides, glowing pain points on head, neck and back"></div>
  <div class="illustration xray" role="img" aria-label="X-ray style view of a neck with the cervical spine highlighted in red"></div>
  <div class="illustration head-icon" role="img" aria-label="Icon of a head tilting forward with a curved arrow"></div>

  <div class="symptom" style="left:42px;top:263px;width:91px">HEADACHES</div>
  <div class="symptom" style="left:42px;top:293px;width:91px">NECK PAIN</div>
  <div class="symptom" style="left:18px;top:321px;width:115px">SHOULDER PAIN</div>
  <div class="symptom" style="left:54px;top:346px;width:79px">BACK PAIN</div>
  <div class="symptom" style="left:10px;top:381px;width:128px">ARMS &amp; HAND PAIN</div>
  <div class="symptom" style="left:54px;top:406px;width:80px">SCIATICA</div>

  <p class="chart-note"><strong>AS THE HEAD TILTS FORWARD.</strong><br>MORE FORCE IS PLACED<br>ON THE SPPINE</p>
  <div class="bar-value" style="left:358px;top:427px;width:22px;font-size:15px">12</div>
  <div class="bar-value" style="left:390px;top:409px;width:24px">27</div>
  <div class="bar-value" style="left:422px;top:396px;width:23px">40</div>
  <div class="bar-value" style="left:457px;top:379px;width:23px">49</div>
  <div class="bar-value" style="left:490px;top:362px;width:24px">60</div>
  <div class="degrees">0° 15° 30° 45° 60°</div>
  <div class="axis-label axis-x">DEGREES OF FORWARD HEAD TILT</div>
  <div class="axis-label axis-y">PRESSURE ON SPINE (LBS)</div>

  <div class="usage">
    <div class="small">THE AVERAGE PERSON SPENDS</div>
    <div class="big">8-11 HOURS PER DAY</div>
    <div class="small">USING ELECTRONIC DEVICES</div>
  </div>

  <div class="contact-band"></div>

  <p class="message">
    <span class="accent">CHIROPRACTIC CARE</span> CAN HELP<br>
    CORRECT AND PREVENT THESE<br>
    PROBLEMS BY <span class="accent">RESTORING</span> AND<br>
    <span class="accent">MAINTAINING PROPER ALIGNMENT</span><br>
    OF THE <span class="accent">NECK</span>
  </p>

  <div class="portrait" role="img" aria-label="Portrait photo of the chiropractor"></div>

  <p class="contact">
    DR. SAMUEL HARLOW<br>
    NOW IN 42 MARLOW STREET,<br>
    EASTVALE 6999<br>
    OFF INITIAL CONSULTATION.<br>
    CALL 0400 555 018<br>
    TO MAKE AN APPOINTMENT.
  </p>

  <footer class="footer">
    <span class="cta">BOOK APPOINTMENT ONLINE --&gt;</span>
    <span class="url">www.spinewellcare.example</span>
  </footer>
</main>
</body>
</html>
```